Mango Grove Indian Restaurants 2019 Menu

Hi,
Please find attached menu text in pdf format. It contains 4 pages. Please work on the menu pages. I will further work with the winner to add the cover page and images as an extended project

Please visit www.mangogroveeats.com.au for more information

```html
<!DOCTYPE html>
<html lang="en">
<head>
<meta charset="utf-8">
<title>Mango Grove – Breads &amp; Desserts Menu</title>
<link href="https://fonts.googleapis.com/css2?family=Lato:wght@400;700&family=Oswald:wght@500&family=Rokkitt:wght@700&family=Playfair+Display:ital,wght@1,700&display=swap" rel="stylesheet">
<style>
  :root{
    --backdrop:#ececec;
    --paper:#ffffff;
    --pattern-pink:#fbe6ec;
    --red-top:#8c0a0b;
    --red-bottom:#c5161d;
    --pink:#f29aab;
    --pink-soft:#f4b3c0;
    --rule:#e9707f;
    --ink:#3a3a3a;
    --brand:#8e1116;
    --grey:#8b8b8b;
    --nf:#7fdc5a;
    --gf:#7cc7e6;
    --veg:#e05aa4;
    --vegan:#e6ef8a;
  }
  *{box-sizing:border-box;margin:0;padding:0}
  html,body{width:1200px;height:1200px;overflow:hidden;background:var(--backdrop)}
  .menu{position:absolute;left:210px;top:50px;width:780px;height:1100px;display:flex;box-shadow:0 2px 10px rgba(0,0,0,.12)}
  .menu__side{position:relative;width:259px;height:100%;background:var(--paper)}
  .side-pattern{position:absolute;inset:0;background:radial-gradient(circle at 40% 55%,var(--pattern-pink) 0%,rgba(251,230,236,.35) 45%,var(--paper) 80%)}
  .brand{position:absolute;top:36px;left:0;width:100%;text-align:center;color:var(--brand)}
  .brand__the{font:italic 700 17px/1 "Playfair Display",serif;color:var(--ink)}
  .brand__name{font:700 25px/1.05 "Lato",sans-serif;margin-top:6px;letter-spacing:.5px}
  .brand__kind{font:italic 700 17px/1 "Playfair Display",serif;color:var(--ink);margin-top:8px}
  .side-title{position:absolute;left:95px;top:232px}
  .tagline{position:absolute;left:28px;bottom:38px;font:400 10.5px/1.25 "Lato",sans-serif;letter-spacing:2.4px;color:var(--grey)}
  .menu__main{position:relative;flex:1;height:100%;background:linear-gradient(180deg,var(--red-top) 0%,var(--red-bottom) 100%)}
  .band-title{position:absolute;left:0;width:100%;text-align:center;font:500 19px/1 "Oswald",sans-serif;letter-spacing:2.5px;color:var(--pink)}
  .rule{position:absolute;left:0;width:100%;height:1px;background:var(--rule)}
  .vrule{position:absolute;width:1px;background:var(--rule)}
  .item{position:absolute;width:180px;color:var(--pink)}
  .item__head{display:flex;justify-content:space-between;align-items:center;font:400 16.5px/1 "Lato",sans-serif;letter-spacing:.3px;margin-bottom:8px}
  .item__text{font:400 8.6px/15.5px "Lato",sans-serif;text-transform:uppercase;color:var(--pink-soft)}
  .justify{text-align:justify}
  .tags{display:flex;gap:3px}
  .tag{width:11px;height:11px;border-radius:50%;font:700 5px/11px "Lato",sans-serif;text-align:center;color:#fff}
  .tag--nf{background:var(--nf)} .tag--gf{background:var(--gf)} .tag--v{background:var(--veg)} .tag--vg{background:var(--vegan)}
  .list{list-style:none;font:400 8.6px/15.5px "Lato",sans-serif;text-transform:uppercase;color:var(--pink-soft)}
  .list li{position:relative;padding-left:19px}
  .list li::before{content:"";position:absolute;left:0;top:6px;width:4px;height:4px;border-radius:50%;background:var(--pink)}
  .list--wide li{line-height:19.5px;padding-left:24px}
  .list--wide li::before{top:8px}
  .notes{list-style:none;color:var(--pink)}
  .notes li{position:relative;padding-left:19px;margin-bottom:12px}
  .notes li::before{content:"";position:absolute;left:0;top:5px;width:4px;height:4px;border-radius:50%;background:var(--pink)}
  .notes strong{display:block;font:700 12px/1.1 "Lato",sans-serif}
  .notes span{display:block;padding-left:12px;font:400 8.6px/13px "Lato",sans-serif;color:var(--pink-soft)}
</style>
</head>
<body>
<div class="menu">
  <aside class="menu__side">
    <div class="side-pattern" role="img" aria-label="Faint pink mandala line pattern across the side panel"></div>
    <div class="brand">
      <p class="brand__the">the</p>
      <p class="brand__name">MANGO<br>GROVE</p>
      <p class="brand__kind">indian restaurant</p>
    </div>
    <svg class="side-title" width="70" height="694" viewBox="0 0 70 694" aria-label="Breads &amp; Desserts">
      <text transform="translate(60 694) rotate(-90)" x="0" y="0" textLength="694" lengthAdjust="spacingAndGlyphs" font-family="Rokkitt, serif" font-weight="700" font-size="82" fill="none" stroke="#f29aab" stroke-width="1.6">BREADS<tspan font-size="40" dy="-8">&amp;</tspan><tspan dy="8">DESSERTS</tspan></text>
    </svg>
    <p class="tagline">YOUR BEST INDIAN RESTAURANT<br>IN PERTH'S NORTHERN SUBURBS</p>
  </aside>

  <main class="menu__main">
    <h2 class="band-title" style="top:24px">BREADS $5</h2>
    <div class="rule" style="top:68px"></div>
    <div class="vrule" style="left:260px;top:114px;height:467px"></div>

    <section class="item" style="left:42px;top:114px">
      <div class="item__head"><span>NAAN</span><span class="tags"><i class="tag tag--nf">NF</i></span></div>
      <p class="item__text">Leavened flat bread, traditionally baked by slapping the bread dough onto the side of a tandoor oven. Dough is made with plain flour, eggs, full cream milk and leavening agents.</p>
      <ul class="list" style="margin-top:32px">
        <li>Butter</li><li>Cheese</li><li>Chilli</li><li>Chilli garlic</li><li>Chocolate</li><li>Garlic</li><li>Kashmiri*</li><li>Kheema**</li><li>Peshwari***</li><li>Plain</li>
      </ul>
      <ul class="notes" style="margin-top:36px">
        <li><strong>*KASHMIRI</strong><span>DRIED FRUITS &amp; NUTS</span></li>
        <li><strong>**KHEEMA</strong><span>LAMB MINCE</span></li>
        <li><strong>**PESHWARI</strong><span>DRIED FRUITS, NUTS,<br>ALMONDS,<br>DESICCATED COCONUT</span></li>
      </ul>
    </section>

    <section class="item" style="left:301px;top:114px">
      <div class="item__head"><span>ROTI</span><span class="tags"><i class="tag tag--nf">NF</i><i class="tag tag--v">DF</i><i class="tag tag--vg">V</i></span></div>
      <p class="item__text justify">Unleavened flat bread, traditionally baked by slapping the bread dough onto the side of a tandoor oven. Dough is made with wheat flour, plain flour and oil.</p>
    </section>

    <section class="item" style="left:301px;top:265px">
      <div class="item__head"><span>PARATHA</span><span class="tags"><i class="tag tag--nf">NF</i></span></div>
      <p class="item__text justify">Unleavened layered flat bread, traditionally baked by slapping the bread dough onto the side of a tandoor oven. Dough is made with wheat flour, plain flour, butter and oil.</p>
      <ul class="list list--wide" style="margin-top:2px">
        <li>Aloo (potato)</li><li>Gobi (cauliflower)</li><li>Aloo gobi</li><li>Plain</li>
      </ul>
    </section>

    <div class="rule" style="top:620px"></div>
    <h2 class="band-title" style="top:645px">DESSERTS $2</h2>
    <div class="rule" style="top:687px"></div>
    <div class="vrule" style="left:260px;top:726px;height:334px"></div>

    <section class="item" style="left:42px;top:722px;width:200px">
      <div class="item__head"><span>COCONUT PUDDING</span><span class="tags"><i class="tag tag--gf">GF</i><i class="tag tag--nf">NF</i></span></div>
      <p class="item__text">Slow cooked coconut milk in full cream milk with cream, sugar and thickening agent.</p>
    </section>
    <section class="item" style="left:42px;top:825px;width:198px">
      <div class="item__head"><span>CUSTARD</span><span class="tags"><i class="tag tag--nf">NF</i></span></div>
      <p class="item__text justify">Slow cooked custard powder in full cream milk with sugar and vanilla essence for added flavour</p>
    </section>
    <section class="item" style="left:42px;top:927px;width:198px">
      <div class="item__head"><span>GULAB JAMUN</span><span class="tags"><i class="tag tag--nf">NF</i></span></div>
      <p class="item__text justify">Soft to firm body, smooth textured fried dumpling traditionally made of milk powder, thickened cream, yoghurt, plain flour and baking powder. It is then soaked in sugar syrup with green cardamom and cloves.</p>
    </section>

    <section class="item" style="left:281px;top:722px;width:198px">
      <div class="item__head"><span>MANGO PUDDING</span><span class="tags"><i class="tag tag--gf">GF</i><i class="tag tag--nf">NF</i></span></div>
      <p class="item__text">Slow cooked sweetened alphonso mango pulp in cream with sugar and thickening agent.</p>
    </section>
    <section class="item" style="left:281px;top:825px;width:198px">
      <div class="item__head"><span>SEMIYA PAYASAM</span><span class="tags"><i class="tag tag--nf">NF</i></span></div>
      <p class="item__text justify" style="line-height:13px">Slow cooked vermicelli (made from hard wheat flour) in full cream milk with saffron, cane sugar, cardamom powder and rose water</p>
    </section>
    <section class="item" style="left:281px;top:950px;width:198px">
      <div class="item__head"><span>SUJI HALWA</span><span class="tags"><i class="tag tag--v">DF</i><i class="tag tag--vg">V</i></span></div>
      <p class="item__text justify" style="line-height:13px">Semolina based sweet dish made with white sugar, raisins and cashew nuts.</p>
    </section>
  </main>
</div>
</body>
</html>
```